Regional Showdown Flyer for Holiday Program

Need a one page flyer, can be back to front or one page, ensuring you can fit all information, colourful, aimed at a market of 8-13 year old boys and girls.
The flyer needs to be noticed, needs to have certain information on it and needs to be Autralian Rule Football orientated.
Have uploaded file so you can understand the style (not content), style of flyer I am looking at getting submitted.

Target Market(s)

8-13 year old boys and girls and their parents.

Requirements
Must have
• Regional Showdown Event
• Price for Regional Showdown Day will be $85
• Strictly Limited Places, only the best footballers should enter this challenge
• Inaugural event, be the first Regional Showdown Winner for your age!
• Do you love a challenge! Put yourself to the test!
• Are you up to it - Water Slide Goal Kicking Contest! The fastest kick in the West (tested by our very own speed gun)! Can you survive the Footy Titan Trail or Last One Standing Goal Kicking! These challenges are crazy are super fun!
• If you think you can deliver on the big stage then this is for YOU!
• All District age winners will receive prizes, awards and the adulation from all their peers!
• Year's 3-5 from 9am to 12pm
• Year's 6-8 from 1-4pm
• All challengers compete against their own age
• Lunch Provided
• Monday 16th April - Upper Tarrowby Regional Showdown Day at Tarrowby Oval
• Tuesday 17th April - North Tarrowby Regional Showdown Day at Kilmorna Reserve
• Wednesday 18th April - Yarlo Regional Showdown Day - Dunhaven Football Club
• Every Challenge Participant receives a District Football!
• Need to put all 3 District Football Logos on the bottom of the flyer, logos attached at bottom.
Nice to have
• Plenty of colour, if you can fit all information on one page that would be fine
Should not have
• Dull, boring, any footballs should be Aussie Rules footballs not NFL or soccer

```html
<!DOCTYPE html>
<html lang="en">
<head>
<meta charset="utf-8">
<title>Regional Showdown Flyer</title>
<link href="https://fonts.googleapis.com/css2?family=Lato:ital,wght@0,400;0,700;0,900;1,700;1,900&display=swap" rel="stylesheet">
<style>
  :root {
    --page-bg: #e9e6e2;
    --navy: #1d4a8c;
    --navy-deep: #173f7a;
    --rule: #3a6fb0;
    --sky-top: #2f6aa8;
    --sky-mid: #4b8cc8;
    --sky-light: #8fc0e6;
    --white: #ffffff;
    --ink: #2b3f5f;
    --strip: #2a5595;
  }
  * { box-sizing: border-box; margin: 0; padding: 0; }
  html, body { width: 1200px; height: 1000px; overflow: hidden; }
  body {
    background: var(--page-bg);
    font-family: "Lato", Arial, sans-serif;
    position: relative;
  }
  .flyer {
    position: absolute;
    left: 270px; top: 32px;
    width: 660px; height: 935px;
    background: var(--white);
    box-shadow: 0 6px 24px rgba(0,0,0,.18);
    overflow: hidden;
  }
  /* Header */
  .masthead { height: 218px; padding: 20px 20px 0; text-align: center; }
  .event-title {
    font-style: italic; font-weight: 900; color: var(--navy);
    font-size: 32px; letter-spacing: .3px; line-height: 1;
    padding-bottom: 12px; border-bottom: 1.5px solid var(--rule);
  }
  .headline {
    font-weight: 900; color: var(--navy-deep);
    font-size: 40px; line-height: 1; margin-top: 10px;
  }
  .subhead {
    font-weight: 400; color: var(--navy);
    font-size: 29px; line-height: 1.1;
    padding-bottom: 8px; border-bottom: 1.5px solid var(--rule);
  }
  .tagline { font-size: 17px; color: var(--ink); margin-top: 12px; }
  .tagline strong { color: var(--navy-deep); font-weight: 900; }

  /* Blue panel */
  .challenge-panel { position: relative; height: 623px; color: var(--white); }
  .sky-backdrop {
    position: absolute; inset: 0;
    background: linear-gradient(180deg, var(--sky-top) 0%, var(--sky-mid) 55%, var(--sky-light) 100%);
  }
  .hero-photo {
    position: absolute; right: 0; top: 0; width: 340px; height: 100%;
    background: linear-gradient(180deg, rgba(60,120,190,.0) 0%, rgba(120,60,50,.35) 45%, rgba(180,40,40,.55) 100%);
  }
  .panel-copy {
    position: relative; width: 330px; margin-left: 27px; padding-top: 16px;
    text-shadow: 0 1px 2px rgba(0,0,0,.25);
  }
  .price { font-size: 22px; line-height: 1.25; font-weight: 400; }
  .limited { font-size: 14px; line-height: 1.3; margin-top: 4px; }
  .divider { border: 0; border-top: 1px solid rgba(255,255,255,.7); margin: 12px 0 4px; }
  .section-title { font-size: 29px; font-weight: 900; line-height: 1.05; }
  .contest { font-size: 13.5px; font-weight: 900; }
  .body-copy { font-size: 13.5px; line-height: 1.32; }
  .callout { font-size: 13.5px; font-weight: 700; line-height: 1.3; margin-top: 10px; }
  .details { font-size: 12px; line-height: 1.32; margin-top: 12px; }
  .details strong { font-weight: 900; }
  .schedule { margin-top: 14px; font-size: 12.5px; line-height: 1.25; }
  .schedule dt { font-weight: 900; }
  .schedule dd { font-size: 11px; margin-bottom: 4px; }
  .giveaway { font-size: 21px; font-weight: 900; line-height: 1.25; margin-top: 20px; }

  /* Footer */
  .club-bar { position: relative; height: 94px; background: var(--white); }
  .club-bar::after {
    content: ""; position: absolute; left: 0; right: 0; bottom: 0; height: 12px;
    background: var(--strip);
  }
  .club {
    position: absolute; top: -16px; width: 150px; height: 92px;
    display: flex; align-items: center; justify-content: center; gap: 8px;
  }
  .club-bump {
    position: absolute; top: 0; left: 37px; width: 76px; height: 76px;
    border-radius: 50%; background: var(--white); z-index: 0;
  }
  .club-name {
    position: relative; z-index: 1; font-weight: 900; font-size: 15px;
    color: var(--navy); line-height: 1.05; text-align: center; margin-top: 18px;
  }
  .club-dot {
    position: relative; z-index: 1; width: 14px; height: 14px; border-radius: 50%;
    background: var(--navy); margin-top: 18px;
  }
  .club--west { left: 28px; }
  .club--centre { left: 240px; }
  .club--east { left: 450px; }
</style>
</head>
<body>
  <main class="flyer">
    <header class="masthead">
      <h1 class="event-title">REGIONAL SHOWDOWN EVENT</h1>
      <p class="headline">DO YOU LOVE A CHALLENGE!</p>
      <p class="subhead">PUT YOURSELF TO THE TEST!</p>
      <p class="tagline">Inaugural event, be the first Regional Showdown <strong>Winner</strong> for your age!</p>
    </header>

    <section class="challenge-panel">
      <div class="sky-backdrop"></div>
      <div class="hero-photo" role="img" aria-label="Young footballer in a red and black jersey, seen from behind, reaching up to mark an Aussie Rules football against a blue sky"></div>

      <div class="panel-copy">
        <p class="price">Price for Regional Showdown Day will be $85</p>
        <p class="limited">Strictly Limited Places, only the best footballers should enter this challenge.</p>
        <hr class="divider">
        <h2 class="section-title">ARE YOU UP TO IT</h2>
        <p class="contest">Water Slide Goal Kicking Contest!</p>
        <p class="body-copy">The fastest kick in the West (tested by our very own speed gun)! Can you survive the Footy Titan Trail or Last One Standing Goal Kicking! These challenges are crazy are super fun!</p>
        <hr class="divider">
        <p class="callout">If you think you can deliver on the big stage then this is for YOU!</p>
        <p class="details">All District age winners will receive prizes, awards and the adulation from all their peers!<br>
          <strong>Year's 3-5 from 9am to 12pm<br>
          Year's 6-8 from 1-4pm<br>
          All challengers compete against their own age<br>
          Lunch Provided</strong></p>
        <dl class="schedule">
          <dt>Monday 16th April</dt>
          <dd>Upper Tarrowby Regional Showdown Day at Tarrowby Oval</dd>
          <dt>Tuesday 17th April</dt>
          <dd>North Tarrowby Regional Showdown Day at Kilmorna Reserve</dd>
          <dt>Wednesday 18th April</dt>
          <dd>Yarlo Regional Showdown Day - Dunhaven Football Club</dd>
        </dl>
        <p class="giveaway">Every Challenge Participant receives a District Football!</p>
      </div>
    </section>

    <footer class="club-bar">
      <div class="club club--west">
        <span class="club-bump"></span>
        <span class="club-name">YARLO<br>DISTRICT</span>
        <span class="club-dot"></span>
      </div>
      <div class="club club--centre">
        <span class="club-bump"></span>
        <span class="club-name">ROVERS<br>DISTRICT</span>
        <span class="club-dot"></span>
      </div>
      <div class="club club--east">
        <span class="club-bump"></span>
        <span class="club-name">MARLINS<br>DISTRICT</span>
        <span class="club-dot"></span>
      </div>
    </footer>
  </main>
</body>
</html>
```